yourSmileCare Brookvale Business Card

Please design a two sided business card that is Elegant and Professional
Add subtle elegant patterns to suit Spot UV printing/ or raised printing

Name: Dr Marcus T. Fenwick
Qualification: BDSc (QLD)
Title: Dental Surgeon, Clinical Director
Company: yourSmileCare Brookvale
Phone: (02) 7593 2268
Address: Shop 7/18-20 Lindon Ave Brookvale 2097
email: info@yoursmilecarebrookvale.com.au
Facebook: facebook.com/yoursmilecarebrookvale

Motto:
Quality dentistry you can trust

Description of services (not compulsory):
Preventative Dentistry | General Dentistry
Cosmetic Dentistry | Teeth Whitening
Crown and Bridge | Root Canal Therapy
Veneers | Clearvono | Orthodontics
Emergency Dental Care | After Hours

Personalised Treatment Plans
Transparent Fees

Please make sure card is elegant and professional

Target Market(s)

general population, patients,
Dental sales companies, other professions

Industry/Entity Type

Dental Clinic

Contact Information for Business Card

Name: Dr Marcus T. Fenwick
Qualification: BDSc (QLD)
Phone: (02) 7593 2268
Address: Shop 7/18-20 Lindon Ave Brookvale

Motto:

Description of services (not compulsory)

Transparent Fees

Image of dental surgery optional

Please make sure card is elegant and profession

Requirements
Must have
• Logo
• Name, Title (next to name), Business
• Phone, address, facbeook
• Must have stylish design to suit SPOT UV reflective printing
Nice to have
• Subtle elegant patterns which will have Spot UV on them when printed
• Colours to match logo colour
• Description of services
Should not have
• Small fonts that are hard to read
• DO NOT PUT IMAGES OF DENTAL INSTRUMENTS OR TEETH PLEASE

```html
<!DOCTYPE html>
<html lang="en">
<head>
<meta charset="utf-8">
<title>yourSmileCare Brookvale – Business Card</title>
<link rel="stylesheet" href="https://fonts.googleapis.com/css2?family=Roboto:wght@400;500&display=swap">
<style>
  :root {
    --brand-green: #7cc242;
    --text-grey: #58595b;
    --card-white: #ffffff;
    --backdrop: #e9eaeb;
    --font-main: "Roboto", Arial, sans-serif;
  }
  * { box-sizing: border-box; margin: 0; padding: 0; }
  html, body {
    width: 1200px;
    height: 1200px;
    overflow: hidden;
    background: var(--backdrop);
    font-family: var(--font-main);
  }
  .canvas {
    width: 1200px;
    height: 1200px;
    display: flex;
    flex-direction: column;
    align-items: center;
    justify-content: center;
    gap: 64px;
  }
  .card {
    width: 860px;
    height: 492px;
    background: var(--card-white);
    border: 22px solid var(--brand-green);
    box-shadow: 0 10px 28px rgba(0,0,0,0.12);
    display: flex;
    flex-direction: column;
    align-items: center;
    justify-content: center;
    text-align: center;
    color: var(--text-grey);
  }
  /* Back: brand + services */
  .brand {
    display: flex;
    align-items: center;
    gap: 14px;
    margin-bottom: 44px;
  }
  .brand-dot {
    width: 26px;
    height: 26px;
    border-radius: 50%;
    background: var(--brand-green);
  }
  .brand-name {
    font-size: 52px;
    font-weight: 500;
    color: var(--brand-green);
    letter-spacing: -0.5px;
  }
  .services-heading {
    font-size: 20px;
    font-weight: 500;
    color: var(--brand-green);
    text-transform: uppercase;
    margin-bottom: 10px;
  }
  .services-line {
    font-size: 20px;
    line-height: 1.45;
  }
  /* Front: contact */
  .doctor-name {
    font-size: 44px;
    font-weight: 500;
    color: var(--brand-green);
    text-transform: uppercase;
    letter-spacing: -0.5px;
    margin-bottom: 10px;
  }
  .credential, .role {
    font-size: 24px;
    line-height: 1.4;
  }
  .contact {
    margin-top: 34px;
    font-size: 24px;
    line-height: 1.45;
  }
</style>
</head>
<body>
<main class="canvas">
  <section class="card card-back" aria-label="Card back">
    <div class="brand">
      <span class="brand-dot"></span>
      <span class="brand-name">yourSmileCare Brookvale</span>
    </div>
    <h2 class="services-heading">Description of services</h2>
    <p class="services-line">Preventative Dentistry | General Dentistry</p>
    <p class="services-line">Cosmetic Dentistry | Teeth Whitening | Crown and Bridge | Root Canal Therapy</p>
    <p class="services-line">Veneers | Clearvono | Orthodontics | Emergency Dental Care | After Hours</p>
  </section>

  <section class="card card-front" aria-label="Card front">
    <h1 class="doctor-name">Dr Marcus T. Fenwick</h1>
    <p class="credential">BDSc (QLD)</p>
    <p class="role">Dental Surgeon, Clinical Director</p>
    <div class="contact">
      <p class="phone">(02) 7593 2268</p>
      <p class="social">yoursmilecarebrookvale</p>
      <p class="address">Shop 7/18-20 Lindon Ave Brookvale</p>
    </div>
  </section>
</main>
</body>
</html>
```